DIN A5 flyer front already exists for the sales outlet

Hi. I'd like to create a DIN A5 flyer. The front should be your design. On the back, I'd like to include more information about our business.
The back should contain (images still need to be added):
Our services
Stamps – Buying and Selling
Whether you're looking for the Lorren Swallow, classic rarities, or the latest stamp issues – we offer almost everything you need for your collection. We're happy to order any stamps we don't currently have in stock. Do you want to sell a stamp collection or have you inherited one? We offer personalized consultations and will make you a fair offer.
Coins – Buying and Selling
From historical cantonal coins and Swiss federal coins dating back to 1850, to coveted gold coins – collectors and investors will find what they're looking for with us. Whether it's a 100-franc Seraphine, rare Batzen, or the Tessin gold Seraphine – we trade with passion and expertise. We are also happy to purchase your coin collection or individual valuable pieces.
Purchase of scrap gold and precious metals
We buy scrap gold, jewelry, watches, rings, gold coins, silver coins, silver billets, silver bars, and other precious metals at fair and transparent prices. Thanks to our many years of experience, you will receive a professional appraisal and market-based purchase prices – discreetly and without obligation.
Postage service for businesses
Save on postage costs: Businesses can purchase valid postage stamps from us at a discounted rate. A simple and attractive way to permanently reduce the shipping costs of your business mail.
Visit us at our new location:
Lindenhofweg 38, 4057 Basel
Feldhaus-Brenner AG – Your specialist shop for stamps, coins and precious metals.
People who want to sell their scrap gold, stamps or coins

```html
<!DOCTYPE html>
<html lang="en">
<head>
<meta charset="utf-8">
<title>Feldhaus-Brenner AG – Our Services</title>
<link href="https://fonts.googleapis.com/css2?family=Cinzel:wght@500;600;700&family=Open+Sans:ital,wght@0,400;0,600;0,700;1,600&display=swap" rel="stylesheet">
<style>
:root{
  --navy:#1f2466;
  --navy-dark:#161a52;
  --gold:#d8ad55;
  --gold-line:#e3c98f;
  --red:#d2141c;
  --card:#f1f1f8;
  --ink:#2a2d4a;
  --page:#f6f5f3;
  --white:#ffffff;
}
*{margin:0;padding:0;box-sizing:border-box}
html,body{width:1200px;height:1137px;overflow:hidden;background:var(--page)}
body{position:relative;font-family:"Open Sans",Arial,sans-serif;color:var(--ink)}
.flyer{position:absolute;left:250px;top:52px;width:728px;height:1036px;background:var(--white);box-shadow:0 2px 10px rgba(0,0,0,.12);overflow:hidden}
.header{position:absolute;left:0;top:0;width:728px;height:200px}
.brand{position:absolute;top:26px;left:0;width:728px;display:flex;justify-content:center;align-items:center;gap:10px}
.brand-mark{width:20px;height:20px;background:var(--red)}
.brand-name{font-family:"Open Sans",Arial,sans-serif;font-weight:700;font-size:20px;color:var(--white);letter-spacing:1px}
.title{position:absolute;top:76px;left:0;width:728px;text-align:center;font-family:"Cinzel",serif;font-weight:600;font-size:46px;color:var(--gold);letter-spacing:1px}
.card{position:absolute;width:326px;height:350px;background:var(--card);border:1.5px solid var(--gold-line);border-radius:8px;overflow:hidden}
.card-head{position:absolute;left:0;top:0;width:326px;height:140px}
.card-title{position:absolute;font-family:"Cinzel",serif;font-weight:600;color:var(--gold);font-size:44px;line-height:1}
.card-sub{position:absolute;font-weight:600;color:var(--white);font-size:17px;letter-spacing:.3px}
.rule{position:absolute;width:52px;height:3px;background:var(--red)}
.icon{position:absolute;width:64px;height:64px;border-radius:50%;background:var(--red);display:flex;align-items:center;justify-content:center}
.body{position:absolute;font-size:15px;line-height:1.25;color:var(--ink)}
.note{position:absolute;font-size:14.4px;line-height:1.3;font-style:italic;font-weight:600;color:var(--navy-dark)}
.stamps{left:31px;top:191px}
.coins{left:372px;top:191px}
.gold{left:31px;top:556px}
.postage{left:372px;top:560px}
.art{position:absolute}
.footer-sky{position:absolute;left:28px;top:918px;width:212px;height:100px;background:linear-gradient(180deg,#f7eed8,#e9d3a2)}
.visit{position:absolute;left:258px;top:922px;width:252px;height:46px}
.visit-text{position:absolute;left:258px;top:926px;width:252px;text-align:center;font-family:"Cinzel",serif;font-weight:600;color:var(--white);font-size:18px;line-height:1.05}
.address{position:absolute;left:258px;top:974px;width:252px;text-align:center;font-family:"Cinzel",serif;font-weight:600;font-size:19px;color:var(--navy);line-height:1.15}
.address .city{color:var(--red)}
.address-rule{position:absolute;top:999px;height:1px;width:252px;left:258px;background:var(--gold-line)}
.map{position:absolute;left:527px;top:918px;width:168px;height:100px;border:1.5px solid var(--gold-line);border-radius:4px;background:linear-gradient(135deg,#eceef2,#dde1e8)}
</style>
</head>
<body>
<main class="flyer">
  <div class="header">
    <svg width="728" height="200" viewBox="0 0 728 200" aria-hidden="true">
      <defs><linearGradient id="navyGrad" x1="0" x2="1"><stop offset="0" stop-color="#1b1f5e"/><stop offset="1" stop-color="#262c78"/></linearGradient></defs>
      <path d="M0 0H728V120Q520 190 300 160Q140 138 0 95Z" fill="url(#navyGrad)"/>
      <path d="M0 112Q150 150 310 170Q520 195 728 128" fill="none" stroke="var(--red)" stroke-width="5"/>
      <path d="M0 120Q160 165 320 178Q520 198 728 138" fill="none" stroke="var(--red)" stroke-width="1.5"/>
    </svg>
    <div class="brand"><span class="brand-mark"></span><span class="brand-name">FELDHAUS-BRENNER AG</span></div>
    <h1 class="title">OUR SERVICES</h1>
  </div>

  <section class="card stamps">
    <svg class="card-head" viewBox="0 0 326 140" aria-hidden="true"><path d="M0 0H326V100Q200 112 0 150Z" fill="var(--navy)"/></svg>
    <h2 class="card-title" style="left:137px;top:20px">STAMPS</h2>
    <p class="card-sub" style="left:137px;top:56px">BUYING &amp; SELLING</p>
    <span class="rule" style="left:140px;top:86px"></span>
    <div class="icon" style="left:248px;top:86px">
      <svg width="34" height="34" viewBox="0 0 34 34" fill="none" stroke="#fff" stroke-width="2.4"><circle cx="17" cy="8" r="5"/><path d="M14 13v6M20 13v6M6 20h22v6H6zM8 30h18"/></svg>
    </div>
    <p class="body" style="left:20px;top:190px;width:270px">Whether you're seeking the Lorren Swallow, classic rarities, or modern stamp issues, we offer a wide selection for collectors.</p>
    <p class="note" style="left:20px;top:281px;width:290px">Looking to sell or have inherited a collection? We provide expert advice, source missing items &amp; make fair offers.</p>
  </section>

  <section class="card coins">
    <svg class="card-head" viewBox="0 0 326 140" aria-hidden="true"><path d="M0 0H326V150Q130 112 0 100Z" fill="var(--navy)"/></svg>
    <h2 class="card-title" style="left:14px;top:20px">COINS</h2>
    <p class="card-sub" style="left:16px;top:56px">BUYING &amp; SELLING</p>
    <span class="rule" style="left:120px;top:86px"></span>
    <div class="icon" style="left:18px;top:86px">
      <svg width="34" height="34" viewBox="0 0 34 34" fill="none" stroke="#fff" stroke-width="2.4"><ellipse cx="12" cy="10" rx="8" ry="3"/><path d="M4 10v12c0 2 16 2 16 0V10M4 16c0 2 16 2 16 0"/><ellipse cx="23" cy="18" rx="8" ry="3"/><path d="M15 18v9c0 2 16 2 16 0v-9M15 23c0 2 16 2 16 0"/></svg>
    </div>
    <p class="body" style="left:20px;top:193px;width:205px">From historic Swiss coins to prized gold coins, we buy and sell a wide range for collectors and investors.</p>
    <p class="note" style="left:20px;top:281px;width:240px">We also purchase coin collections and individual valuable pieces at fair market prices.</p>
  </section>

  <section class="card gold">
    <svg class="card-head" viewBox="0 0 326 140" aria-hidden="true"><path d="M0 0H326V100Q200 112 0 150Z" fill="var(--navy)"/></svg>
    <p class="card-sub" style="left:24px;top:14px">PURCHASE OF</p>
    <h2 class="card-title" style="left:24px;top:36px;font-size:29px;line-height:1">SCRAP GOLD &amp;<br>PRECIOUS METALS</h2>
    <span class="rule" style="left:28px;top:100px"></span>
    <div class="icon" style="left:248px;top:104px">
      <svg width="36" height="34" viewBox="0 0 36 34" fill="none" stroke="#fff" stroke-width="2.2"><path d="M10 18h10l2 6H8zM4 26h12l2 6H2zM20 26h12l2 6H18zM24 4v6M21 7h6M30 12v4M28 14h4"/></svg>
    </div>
    <p class="body" style="left:110px;top:176px;width:206px">We buy scrap gold, jewellery, watches, rings, gold and silver coins, bars, and other precious metals at fair, transparent prices.</p>
    <p class="note" style="left:22px;top:283px;width:290px">Benefit from our expert appraisal, competitive market prices, and discreet, no-obligation service.</p>
  </section>

  <section class="card postage">
    <svg class="card-head" viewBox="0 0 326 140" aria-hidden="true"><path d="M0 0H326V150Q130 112 0 100Z" fill="var(--navy)"/></svg>
    <h2 class="card-title" style="left:16px;top:18px;font-size:29px">POSTAGE SERVICES</h2>
    <p class="card-sub" style="left:18px;top:48px;font-size:16px">OF BUSINESS</p>
    <span class="rule" style="left:20px;top:74px"></span>
    <div class="icon" style="left:17px;top:99px">
      <svg width="32" height="34" viewBox="0 0 32 34" fill="none" stroke="#fff" stroke-width="2.2" stroke-dasharray="3 2"><rect x="4" y="3" width="24" height="28"/><path d="M10 11h12M10 16h12M10 21h8" stroke-dasharray="none"/></svg>
    </div>
    <p class="body" style="left:18px;top:180px;width:195px">Save on postage costs: Businesses can purchase valid postage stamps from us at a discounted rate.</p>
    <p class="note" style="left:18px;top:268px;width:234px">A simple and attractive way to permanently reduce the shipping costs of your business mail.</p>
  </section>

  <div class="art" role="img" aria-label="Classic Swiss postage stamps" style="left:-4px;top:108px;width:108px;height:108px;transform:rotate(-10deg);background:linear-gradient(135deg,#2e8a8e,#1d5d6c)"></div>
  <div class="art" role="img" aria-label="Red cantonal stamp" style="left:26px;top:238px;width:110px;height:118px;background:linear-gradient(135deg,#e9dcc4,#c9816f);border:2px solid #3a3030"></div>
  <div class="art" role="img" aria-label="Gold coin" style="left:580px;top:150px;width:150px;height:150px;border-radius:50%;background:radial-gradient(circle at 40% 35%,#f3d27a,#b98a2a)"></div>
  <div class="art" role="img" aria-label="Silver coin" style="left:600px;top:286px;width:100px;height:100px;border-radius:50%;background:radial-gradient(circle at 45% 35%,#eeeeee,#9a9a9a)"></div>
  <div class="art" role="img" aria-label="Small copper coins" style="left:632px;top:368px;width:90px;height:56px;border-radius:28px;background:radial-gradient(circle at 45% 40%,#d9b08a,#8e6a48)"></div>
  <div class="art" role="img" aria-label="Gold jewellery chains and a watch" style="left:0;top:652px;width:120px;height:178px;border-radius:40%;background:radial-gradient(circle at 50% 50%,#e7bf72,#9c6a23)"></div>
  <div class="art" role="img" aria-label="Vintage Swiss stamps" style="left:634px;top:626px;width:94px;height:300px;background:linear-gradient(180deg,#d9793a,#e8d49a 55%,#d6b36a)"></div>

  <div class="footer-sky" role="img" aria-label="Line illustration of the city skyline"></div>
  <svg class="visit" viewBox="0 0 252 46" aria-hidden="true"><path d="M0 0H252L242 23L252 46H0L10 23Z" fill="var(--red)"/></svg>
  <p class="visit-text">VISIT US AT OUR<br>NEW LOCATION</p>
  <span class="address-rule"></span>
  <p class="address">LINDENHOFWEG 38<br><span class="city">4057 BASEL</span></p>
  <div class="map" role="img" aria-label="Street map showing the shop location"></div>
</main>
</body>
</html>
```